Kinesiology undergraduate program needs an infographic

We would like an infographic to creatively and succinctly inform students, faculty, staff, and others about our undergraduate values and competencies (perhaps also integrating our mission and vision). We would like to see a design that incorporates the definition of Kinesiology (the study of human movement) and the colors of our Westbrook State University at Larkfield.

```html
<!DOCTYPE html>
<html lang="en">
<head>
<meta charset="utf-8">
<title>Kinesiology Undergraduate Program – Mission, Vision, Values</title>
<link rel="stylesheet" href="https://fonts.googleapis.com/css2?family=Montserrat:wght@400;600;700&family=Quicksand:wght@400;500&display=swap">
<style>
:root{
  --blue:#1f3f90;
  --blue-deep:#16307a;
  --red:#d4213f;
  --orange:#f29a2e;
  --gold:#f7a92b;
  --purple:#4b3688;
  --ink:#1b1b1b;
  --white:#ffffff;
}
*{box-sizing:border-box;margin:0;padding:0}
html,body{width:1200px;height:580px;overflow:hidden;background:var(--white)}
.sheet{position:relative;width:1200px;height:580px;background:var(--white)}
.poster{position:absolute;top:13px;width:597px;height:842px;transform:scale(.6615);transform-origin:0 0;overflow:hidden;background:var(--white);font-family:"Quicksand",sans-serif}
.poster--one{left:0}
.poster--two{left:403px}
.poster--three{left:806px}

.hero{position:absolute;left:0;top:0;width:597px;height:200px;background:linear-gradient(100deg,#d9d7d4 0%,#c8b09c 28%,#b89479 45%,#8a8a8c 70%,#6f6f72 100%)}
.hero-curve{position:absolute;left:0;top:120px;width:597px;height:100px}

.statement-row{position:absolute;left:0;top:190px;width:597px;height:225px}
.side-column{position:absolute;left:0;top:185px;width:216px;height:657px;background:linear-gradient(180deg,var(--blue) 0%,var(--blue-deep) 60%,var(--blue) 100%)}
.poster--three .statement-row{background:linear-gradient(90deg,var(--purple) 0%,#3a3a8e 50%,var(--blue) 100%)}

.statement{position:absolute;top:28px;width:180px;text-align:center}
.statement--mission{left:9px}
.statement--vision{left:212px}
.statement--values{left:404px}
.poster--two .statement{top:34px}
.icon{display:block;margin:0 auto;width:28px;height:24px}
.label{display:inline-block;margin-top:2px;width:116px;height:30px;border:1.5px solid var(--orange);font:400 14px/27px "Montserrat",sans-serif;color:var(--orange);letter-spacing:.2px}
.poster--two .statement--mission .label,.poster--three .label{color:var(--white)}
.statement p{margin-top:6px;font-size:15px;line-height:15.5px;color:var(--orange);white-space:nowrap}
.statement--values p{margin-top:34px;font-size:15px;line-height:13px}

.figure-panel{position:absolute;left:0;top:390px;width:222px;height:452px;z-index:1}
.figure-panel svg{width:100%;height:100%;display:block}

.banner{position:absolute;left:0;top:415px;width:597px;height:82px;background:var(--red);z-index:2}
.poster--two .banner{left:216px;width:381px}
.banner h2{position:absolute;left:0;top:19px;width:584px;font:700 16.5px/21px "Montserrat",sans-serif;color:var(--gold);text-align:center;white-space:nowrap}
.poster--two .banner h2{width:246px;top:10px}
.poster--three .banner h2{width:570px}
.banner-figure{position:absolute;right:0;top:0;width:125px;height:82px;background:linear-gradient(135deg,var(--blue) 0%,#2c5fa8 45%,var(--red) 100%)}

.wordmark{position:absolute;left:148px;top:772px;width:135px;font:700 10px/11px "Montserrat",sans-serif;color:var(--red);text-transform:uppercase;transform:rotate(-58deg);transform-origin:0 0;display:flex;align-items:center;gap:4px;z-index:3}
.wordmark-dot{flex:none;width:10px;height:10px;border-radius:50%;background:var(--red)}

.competencies{position:absolute;left:257px;top:520px;width:220px;color:var(--ink);z-index:2}
.poster--two .competencies,.poster--three .competencies{left:268px}
.competencies h3{font:700 8.6px/11px "Montserrat",sans-serif;color:var(--orange);text-transform:uppercase;margin-bottom:6px}
.competencies ul{list-style:none;margin-bottom:19px}
.competencies li{font:400 10px/12px "Montserrat",sans-serif}
.competencies li::before{content:"- "}

.tiles{position:absolute;left:425px;top:505px;width:172px;height:337px;z-index:1}
.tiles svg{width:100%;height:100%;display:block}
</style>
</head>
<body>
<div class="sheet">

  <!-- ============ Variant one ============ -->
  <article class="poster poster--one">
    <div class="hero" role="img" aria-label="Photo of a therapist's hands applying kinesiology tape to a young man's shoulder"></div>
    <svg class="hero-curve" viewBox="0 0 597 100" preserveAspectRatio="none" aria-hidden="true">
      <defs><linearGradient id="curve1" x1="0" x2="1"><stop offset="0" stop-color="#d4213f"/><stop offset=".45" stop-color="#1f3f90"/><stop offset="1" stop-color="#1f3f90"/></linearGradient></defs>
      <path d="M0 62 Q300 70 597 0 L597 20 Q300 90 0 85 Z" fill="url(#curve1)"/>
      <path d="M0 85 Q300 90 597 20 L597 100 L0 100 Z" fill="#fff"/>
    </svg>
    <section class="statement-row">
      <div class="statement statement--mission">
        <svg class="icon" viewBox="0 0 28 24" aria-hidden="true"><circle cx="14" cy="13" r="10" fill="#f29a2e"/><circle cx="14" cy="13" r="6" fill="#fff"/><circle cx="14" cy="13" r="3" fill="#f29a2e"/><path d="M14 13 L25 3" stroke="#d4213f" stroke-width="2"/></svg>
        <span class="label">OUR MISSION</span>
        <p>To empower<br>undergraduate<br>students to pursue<br>excellence through<br>scientific discovery,<br>clinical practice, and<br>health promotion</p>
      </div>
      <div class="statement statement--vision">
        <svg class="icon" viewBox="0 0 28 24" aria-hidden="true"><ellipse cx="14" cy="12" rx="13" ry="7" fill="#f29a2e"/><circle cx="14" cy="12" r="5" fill="#fff"/><circle cx="14" cy="12" r="2.5" fill="#f29a2e"/></svg>
        <span class="label">OUR VISION</span>
        <p>WSUL Kinesiology<br>graduates are<br>leaders who excel<br>in careers that<br>enhance the quality<br>of life of individuals<br>and communities</p>
      </div>
      <div class="statement statement--values">
        <svg class="icon" viewBox="0 0 28 24" aria-hidden="true"><rect x="2" y="6" width="14" height="10" rx="3" fill="#f29a2e" transform="rotate(-15 9 11)"/><rect x="12" y="8" width="14" height="10" rx="3" fill="#f7b95a" transform="rotate(15 19 13)"/></svg>
        <span class="label">OUR VALUES</span>
        <p>Student Success,<br>Science, and<br>Service</p>
      </div>
    </section>
    <div class="figure-panel" role="img" aria-label="Illustration of a running anatomical figure over a blue and red diagonal backdrop">
      <svg viewBox="0 0 222 452" preserveAspectRatio="none"><defs><linearGradient id="fig1" x1="0" y1="0" x2="1" y2="1"><stop offset="0" stop-color="#2d5ea6"/><stop offset=".5" stop-color="#1f3f90"/><stop offset="1" stop-color="#d4213f"/></linearGradient></defs><path d="M0 0 L222 200 L222 452 L0 452 Z" fill="url(#fig1)"/><path d="M136 398 L222 256 L222 322 L170 406 Z" fill="#fff"/></svg>
    </div>
    <section class="banner">
      <h2>Student Success, Science, and Service<br>Our Graduates Will Be Competent In</h2>
      <div class="banner-figure" role="img" aria-label="Illustration of an anatomical figure stretching on tiled panels"></div>
    </section>
    <div class="wordmark"><span class="wordmark-dot"></span><span>Westbrook State University at Larkfield</span></div>
    <section class="competencies">
      <h3>The Science of Kinesiology</h3>
      <ul><li>Foundational Concepts of Kinesiology</li><li>Clinical Application</li><li>Scientific Communication</li></ul>
      <h3>Thinking and Reasoning</h3>
      <ul><li>Critical Thinking</li><li>Quantitative Reasoning</li><li>Scientific Inquiry</li><li>Concept Integration</li></ul>
      <h3>Relationships and Communication</h3>
      <ul><li>Cultural Competence</li><li>Professionalism</li><li>Leadership and Teamwork</li><li>Service Orientation/Citizenship</li></ul>
      <h3>Intrapersonal Growth</h3>
      <ul><li>Cultural Humility/Sensitivity</li><li>Integrity</li><li>Self-Directed</li><li>Dependability</li><li>Mission Oriented</li></ul>
    </section>
    <div class="tiles" role="img" aria-label="Illustration of an anatomical figure in a lunge across diagonal tiles">
      <svg viewBox="0 0 172 337"><defs><linearGradient id="tile1" x1="0" y1="0" x2="1" y2="1"><stop offset="0" stop-color="#2f7bb0"/><stop offset=".55" stop-color="#1f3f90"/><stop offset="1" stop-color="#d4213f"/></linearGradient></defs>
        <path d="M90 70 L172 5 L172 100 L125 145 Z" fill="url(#tile1)"/><path d="M10 140 L85 80 L160 150 L90 225 Z" fill="url(#tile1)"/><path d="M110 215 L172 155 L172 280 Z" fill="url(#tile1)"/><path d="M0 265 L75 200 L150 275 L100 337 L60 337 Z" fill="url(#tile1)"/></svg>
    </div>
  </article>

  <!-- ============ Variant two ============ -->
  <article class="poster poster--two">
    <div class="hero" role="img" aria-label="Photo of a therapist's hands applying kinesiology tape to a young man's shoulder"></div>
    <svg class="hero-curve" viewBox="0 0 597 100" preserveAspectRatio="none" aria-hidden="true">
      <defs><linearGradient id="curve2" x1="0" x2="1"><stop offset="0" stop-color="#d4213f"/><stop offset=".45" stop-color="#1f3f90"/><stop offset="1" stop-color="#1f3f90"/></linearGradient></defs>
      <path d="M0 62 Q300 70 597 0 L597 20 Q300 90 0 85 Z" fill="url(#curve2)"/>
      <path d="M0 85 Q300 90 597 20 L597 100 L0 100 Z" fill="#fff"/>
    </svg>
    <div class="side-column"></div>
    <section class="statement-row">
      <div class="statement statement--mission">
        <svg class="icon" viewBox="0 0 28 24" aria-hidden="true"><circle cx="14" cy="13" r="10" fill="#f29a2e"/><circle cx="14" cy="13" r="6" fill="#fff"/><circle cx="14" cy="13" r="3" fill="#f29a2e"/><path d="M14 13 L25 3" stroke="#d4213f" stroke-width="2"/></svg>
        <span class="label">OUR MISSION</span>
        <p>To empower<br>undergraduate<br>students to pursue<br>excellence through<br>scientific discovery,<br>clinical practice, and<br>health promotion</p>
      </div>
      <div class="statement statement--vision">
        <svg class="icon" viewBox="0 0 28 24" aria-hidden="true"><ellipse cx="14" cy="12" rx="13" ry="7" fill="#f29a2e"/><circle cx="14" cy="12" r="5" fill="#fff"/><circle cx="14" cy="12" r="2.5" fill="#f29a2e"/></svg>
        <span class="label">OUR VISION</span>
        <p>WSUL Kinesiology<br>graduates are<br>leaders who excel<br>in careers that<br>enhance the quality<br>of life of individuals<br>and communities</p>
      </div>
      <div class="statement statement--values">
        <svg class="icon" viewBox="0 0 28 24" aria-hidden="true"><rect x="2" y="6" width="14" height="10" rx="3" fill="#f29a2e" transform="rotate(-15 9 11)"/><rect x="12" y="8" width="14" height="10" rx="3" fill="#f7b95a" transform="rotate(15 19 13)"/></svg>
        <span class="label">OUR VALUES</span>
        <p>Student Success,<br>Science, and<br>Service</p>
      </div>
    </section>
    <div class="figure-panel" role="img" aria-label="Illustration of a running anatomical figure over a blue and red diagonal backdrop">
      <svg viewBox="0 0 222 452" preserveAspectRatio="none"><defs><linearGradient id="fig2" x1="0" y1="0" x2="1" y2="1"><stop offset="0" stop-color="#2d5ea6"/><stop offset=".5" stop-color="#1f3f90"/><stop offset="1" stop-color="#d4213f"/></linearGradient></defs><path d="M0 0 L216 200 L216 452 L0 452 Z" fill="url(#fig2)"/><path d="M136 398 L216 266 L216 330 L170 406 Z" fill="#fff"/></svg>
    </div>
    <section class="banner">
      <h2>Student Success, Science,<br>and Service Our Graduates<br>Will Be Competent In</h2>
      <div class="banner-figure" role="img" aria-label="Illustration of an anatomical figure stretching on tiled panels"></div>
    </section>
    <div class="wordmark"><span class="wordmark-dot"></span><span>Westbrook State University at Larkfield</span></div>
    <section class="competencies">
      <h3>The Science of Kinesiology</h3>
      <ul><li>Foundational Concepts of Kinesiology</li><li>Clinical Application</li><li>Scientific Communication</li></ul>
      <h3>Thinking and Reasoning</h3>
      <ul><li>Critical Thinking</li><li>Quantitative Reasoning</li><li>Scientific Inquiry</li><li>Concept Integration</li></ul>
      <h3>Relationships and Communication</h3>
      <ul><li>Cultural Competence</li><li>Professionalism</li><li>Leadership and Teamwork</li><li>Service Orientation/Citizenship</li></ul>
      <h3>Intrapersonal Growth</h3>
      <ul><li>Cultural Humility/Sensitivity</li><li>Integrity</li><li>Self-Directed</li><li>Dependability</li><li>Mission Oriented</li></ul>
    </section>
    <div class="tiles" role="img" aria-label="Illustration of an anatomical figure in a lunge across diagonal tiles">
      <svg viewBox="0 0 172 337"><defs><linearGradient id="tile2" x1="0" y1="0" x2="1" y2="1"><stop offset="0" stop-color="#2f7bb0"/><stop offset=".55" stop-color="#1f3f90"/><stop offset="1" stop-color="#d4213f"/></linearGradient></defs>
        <path d="M90 70 L172 5 L172 100 L125 145 Z" fill="url(#tile2)"/><path d="M10 140 L85 80 L160 150 L90 225 Z" fill="url(#tile2)"/><path d="M110 215 L172 155 L172 280 Z" fill="url(#tile2)"/><path d="M0 265 L75 200 L150 275 L100 337 L60 337 Z" fill="url(#tile2)"/></svg>
    </div>
  </article>

  <!-- ============ Variant three ============ -->
  <article class="poster poster--three">
    <div class="hero" role="img" aria-label="Photo of a therapist's hands applying kinesiology tape to a young man's shoulder"></div>
    <svg class="hero-curve" viewBox="0 0 597 100" preserveAspectRatio="none" aria-hidden="true">
      <defs><linearGradient id="curve3" x1="0" x2="1"><stop offset="0" stop-color="#d4213f"/><stop offset=".45" stop-color="#1f3f90"/><stop offset="1" stop-color="#1f3f90"/></linearGradient></defs>
      <path d="M0 62 Q300 70 597 0 L597 100 L0 100 Z" fill="url(#curve3)"/>
    </svg>
    <section class="statement-row">
      <div class="statement statement--mission">
        <svg class="icon" viewBox="0 0 28 24" aria-hidden="true"><circle cx="14" cy="13" r="10" fill="#f29a2e"/><circle cx="14" cy="13" r="6" fill="#fff"/><circle cx="14" cy="13" r="3" fill="#f29a2e"/><path d="M14 13 L25 3" stroke="#d4213f" stroke-width="2"/></svg>
        <span class="label">OUR MISSION</span>
        <p>To empower<br>undergraduate<br>students to pursue<br>excellence through<br>scientific discovery,<br>clinical practice, and<br>health promotion</p>
      </div>
      <div class="statement statement--vision">
        <svg class="icon" viewBox="0 0 28 24" aria-hidden="true"><ellipse cx="14" cy="12" rx="13" ry="7" fill="#f29a2e"/><circle cx="14" cy="12" r="5" fill="#fff"/><circle cx="14" cy="12" r="2.5" fill="#f29a2e"/></svg>
        <span class="label">OUR VISION</span>
        <p>WSUL Kinesiology<br>graduates are<br>leaders who excel<br>in careers that<br>enhance the quality<br>of life of individuals<br>and communities</p>
      </div>
      <div class="statement statement--values">
        <svg class="icon" viewBox="0 0 28 24" aria-hidden="true"><rect x="2" y="6" width="14" height="10" rx="3" fill="#f29a2e" transform="rotate(-15 9 11)"/><rect x="12" y="8" width="14" height="10" rx="3" fill="#f7b95a" transform="rotate(15 19 13)"/></svg>
        <span class="label">OUR VALUES</span>
        <p>Student Success,<br>Science, and<br>Service</p>
      </div>
    </section>
    <div class="figure-panel" role="img" aria-label="Illustration of a running anatomical figure over a blue and red diagonal backdrop">
      <svg viewBox="0 0 222 452" preserveAspectRatio="none"><defs><linearGradient id="fig3" x1="0" y1="0" x2="1" y2="1"><stop offset="0" stop-color="#2d5ea6"/><stop offset=".5" stop-color="#1f3f90"/><stop offset="1" stop-color="#d4213f"/></linearGradient></defs><path d="M0 0 L216 200 L216 452 L0 452 Z" fill="url(#fig3)"/><path d="M136 398 L216 266 L216 330 L170 406 Z" fill="#fff"/></svg>
    </div>
    <section class="banner">
      <h2>Student Success, Science, and Service<br>Our Graduates Will Be Competent In</h2>
      <div class="banner-figure" role="img" aria-label="Illustration of an anatomical figure stretching on tiled panels"></div>
    </section>
    <div class="wordmark"><span class="wordmark-dot"></span><span>Westbrook State University at Larkfield</span></div>
    <section class="competencies">
      <h3>The Science of Kinesiology</h3>
      <ul><li>Foundational Concepts of Kinesiology</li><li>Clinical Application</li><li>Scientific Communication</li></ul>
      <h3>Thinking and Reasoning</h3>
      <ul><li>Critical Thinking</li><li>Quantitative Reasoning</li><li>Scientific Inquiry</li><li>Concept Integration</li></ul>
      <h3>Relationships and Communication</h3>
      <ul><li>Cultural Competence</li><li>Professionalism</li><li>Leadership and Teamwork</li><li>Service Orientation/Citizenship</li></ul>
      <h3>Intrapersonal Growth</h3>
      <ul><li>Cultural Humility/Sensitivity</li><li>Integrity</li><li>Self-Directed</li><li>Dependability</li><li>Mission Oriented</li></ul>
    </section>
    <div class="tiles" role="img" aria-label="Illustration of an anatomical figure in a lunge across diagonal tiles">
      <svg viewBox="0 0 172 337"><defs><linearGradient id="tile3" x1="0" y1="0" x2="1" y2="1"><stop offset="0" stop-color="#2f7bb0"/><stop offset=".55" stop-color="#1f3f90"/><stop offset="1" stop-color="#d4213f"/></linearGradient></defs>
        <path d="M90 70 L172 5 L172 100 L125 145 Z" fill="url(#tile3)"/><path d="M10 140 L85 80 L160 150 L90 225 Z" fill="url(#tile3)"/><path d="M110 215 L172 155 L172 280 Z" fill="url(#tile3)"/><path d="M0 265 L75 200 L150 275 L100 337 L60 337 Z" fill="url(#tile3)"/></svg>
    </div>
  </article>

</div>
</body>
</html>
```